Business Card Design

5* Hotel Property based on an island in Greece

My position is aparta from being a director, i'm on the accounts payable too, not sure how this should be stated, with a comma or "/"?

Sorry about the uploaded logo, it was a mistaken one!

There's also need to be added this  www.corvanteholdings.com on the back side of the card!

Also need to have the logo of the corvante holdings which can be found in a second on the brief! Thank you guys, irini

Industry/Entity Type

Business

Contact Information for Business Card

VERISTOKA PELLA Hotel
Irini Dravetsou
Director, AP Dept.

www.veristoka.gr
Peltira Island 85300
Greece

irinidravetsou@fenmail.com
+306951273064

```html
<!DOCTYPE html>
<html lang="en">
<head>
<meta charset="utf-8">
<title>Veristoka Pella Hotel – Business Card</title>
<link rel="stylesheet" href="https://fonts.googleapis.com/css2?family=Cinzel:wght@400;500&family=Open+Sans:wght@400;500&display=swap">
<style>
  :root {
    --page: #ffffff;
    --card: #ffffff;
    --brand-blue: #0a72b9;
    --name-blue: #1677bd;
    --rule-blue: #6cc5ef;
    --mark-blue: #3ab0e6;
    --ink: #3a3a3a;
    --ink-soft: #4a4a4a;
  }
  * { margin: 0; padding: 0; box-sizing: border-box; }
  html, body { width: 1200px; height: 1000px; overflow: hidden; background: var(--page); }
  .canvas { position: relative; width: 1200px; height: 1000px; }

  .card {
    position: absolute; left: 115px; top: 181px; width: 970px; height: 638px;
    background: var(--card);
    box-shadow: 0 10px 28px rgba(0,0,0,0.22);
  }

  .brand { position: absolute; left: 45px; top: 38px; display: flex; align-items: center; }
  .brand-mark { width: 140px; height: 140px; flex: none; }
  .brand-name {
    margin-left: 32px; margin-top: -12px;
    font-family: "Cinzel", serif; font-weight: 400; color: var(--ink-soft);
  }
  .brand-name .line-1 { display: block; font-size: 38px; letter-spacing: 1px; line-height: 1.1; }
  .brand-name .line-2 { display: block; font-size: 24px; letter-spacing: 13px; margin-top: 6px; }

  .identity { position: absolute; left: 223px; top: 245px; width: 524px; text-align: center; }
  .person-name {
    font-family: "Cinzel", serif; font-weight: 400; font-size: 50px;
    color: var(--name-blue); line-height: 64px; letter-spacing: 1px;
  }
  .rule { height: 3px; background: var(--rule-blue); }
  .role {
    margin-top: 14px;
    font-family: "Cinzel", serif; font-size: 26px; color: var(--ink); line-height: 32px;
  }
  .email {
    font-family: "Open Sans", sans-serif; font-size: 23px; color: var(--name-blue);
    line-height: 30px; margin-bottom: 12px;
  }

  .address {
    position: absolute; left: 38px; top: 496px;
    font-family: "Cinzel", serif; font-size: 27px; line-height: 35px; color: var(--name-blue);
  }
  .phone {
    position: absolute; right: 38px; top: 531px;
    font-family: "Cinzel", serif; font-size: 29px; line-height: 35px; color: var(--name-blue);
  }

  .web-band {
    position: absolute; left: 19px; top: 572px; width: 933px; height: 49px;
    background: var(--brand-blue);
    display: flex; align-items: center; justify-content: center;
    font-family: "Open Sans", sans-serif; font-size: 24px; color: #ffffff;
  }
</style>
</head>
<body>
<div class="canvas">
  <section class="card">
    <header class="brand">
      <svg class="brand-mark" viewBox="0 0 140 140" aria-hidden="true">
        <circle cx="70" cy="70" r="66" fill="var(--mark-blue)"/>
      </svg>
      <div class="brand-name">
        <span class="line-1">VERISTOKA PELLA</span>
        <span class="line-2">HOTEL</span>
      </div>
    </header>

    <div class="identity">
      <h1 class="person-name">Irini Dravetsou</h1>
      <div class="rule"></div>
      <p class="role">DIRECTOR, AP DEPT.</p>
      <p class="email">irinidravetsou@fenmail.com</p>
      <div class="rule"></div>
    </div>

    <p class="address">Peltira Island<br>85300 Greece</p>
    <p class="phone">T: +306951273064</p>

    <footer class="web-band">www.veristoka.gr</footer>
  </section>
</div>
</body>
</html>
```